Silver Creek Plumbing Business card & letter head design

We need a new business card and letter head for our plumbing company called silver creek plumbing. attached is the companys logo. We provide domestic and commercial plumbing services in regional western Australia. We are after Something simple yet nice to look at and something that fits within the trade industry.

Target Market(s)

trade/building industry

Contact Information for Business Card

Darl Hensby
Manager
0461 238 574
enquiries@scplumbwork.net.au
ABN: 47 381 905 462
PCL: 5187

Domestic & Commercial Plumbing
Tip Truck & Excavator hire

Colors

Designer to choose colors to be used in the design.

```html
<!DOCTYPE html>
<html lang="en">
<head>
<meta charset="utf-8">
<title>Silver Creek Plumbing – Stationery</title>
<link href="https://fonts.googleapis.com/css2?family=Lato:wght@400;700;900&family=Montserrat:wght@700&display=swap" rel="stylesheet">
<style>
  :root{
    --brand-blue:#0b57a5;
    --ink:#4a4a4a;
    --ink-soft:#6b6b6b;
    --paper:#ffffff;
    --backdrop:#e4e4e4;
  }
  *{box-sizing:border-box;margin:0;padding:0}
  html,body{width:1200px;height:971px;overflow:hidden}
  body{background:var(--backdrop);font-family:'Lato',sans-serif;color:var(--ink);position:relative}

  .letterhead{position:absolute;left:50px;top:35px;width:636px;height:900px;background:var(--paper);
    box-shadow:0 6px 24px rgba(0,0,0,.12);overflow:hidden}
  .letterhead__band{position:absolute;left:0;top:0;width:100%;height:60px}
  .wordmark{font-family:'Lato',sans-serif;font-weight:900;color:var(--brand-blue);text-transform:uppercase;letter-spacing:.04em;display:flex;align-items:center;gap:8px}
  .wordmark__dot{width:10px;height:10px;border-radius:50%;background:var(--brand-blue)}
  .letterhead .wordmark{position:absolute;top:78px;left:0;right:0;justify-content:center;font-size:22px}
  .letter{position:absolute;left:56px;top:160px;width:520px;font-size:11.5px;line-height:1.6;color:var(--ink-soft)}
  .letter__date{margin-bottom:14px}
  .letter__recipient{margin-bottom:26px}
  .letter__greeting{margin-bottom:22px}
  .letter p{margin-bottom:16px}
  .letter__closing{margin-top:18px;margin-bottom:20px}
  .signatory__name{font-family:'Montserrat',sans-serif;font-weight:700;font-size:17px;color:var(--ink)}
  .signatory__role{font-size:12px;color:var(--ink-soft)}
  .signature{display:block;width:180px;height:54px;margin-top:10px;background:linear-gradient(90deg,#dfe7f3,#eef2f8);border-radius:4px}

  .contact{list-style:none;font-size:11.5px;line-height:1.55;color:var(--ink-soft)}
  .contact li{display:flex;align-items:center;gap:8px}
  .contact svg{width:10px;height:10px;flex:none;fill:var(--brand-blue)}
  .contact__reg{color:var(--brand-blue);font-weight:700;padding-left:18px}
  .letterhead .contact{position:absolute;left:56px;bottom:70px}

  .card{position:absolute;width:440px;height:252px;box-shadow:0 6px 20px rgba(0,0,0,.14)}
  .card--front{left:730px;top:170px;background:var(--brand-blue);display:flex;align-items:center;justify-content:center}
  .card--front .wordmark{color:#fff;font-size:22px}
  .card--front .wordmark__dot{background:#fff}
  .card--back{left:730px;top:480px;background:var(--paper);border-top:5px solid var(--brand-blue);padding:40px 44px}
  .card--back .signatory__name{color:var(--brand-blue);font-size:18px}
  .card--back .signatory__role{font-size:10px;margin-bottom:22px}
  .card--back .contact{font-size:10.5px}
</style>
</head>
<body>

<section class="letterhead" aria-label="Letterhead">
  <svg class="letterhead__band" viewBox="0 0 636 60" preserveAspectRatio="none" aria-hidden="true">
    <path d="M0 0 H636 V6 C420 10 200 20 70 48 C40 54 15 52 0 40 Z" fill="var(--brand-blue)"/>
    <path d="M0 34 C15 46 40 48 70 42 C200 14 420 4 636 0 V0 H0Z" fill="#fff"/>
  </svg>

  <div class="wordmark"><span class="wordmark__dot"></span>Silver Creek Plumbing</div>

  <div class="letter">
    <div class="letter__date">03.12.2019</div>
    <div class="letter__recipient">Recipient name<br>54 Harbour Rd.<br>Bunbury, WA 6230</div>
    <div class="letter__greeting">Dear, Mr ____________</div>
    <p>Lorem Ipsum is simply dummy text of the printing and typesetting industry. Lorem Ipsum has been the industry's standard dummy text ever since the1500s,when an unknown printer took a galley of type and scrambled it to make a type specimen book. It has survived not only five centuries, but also the leap into electronic typesetting, remaining essentially unchanged.</p>
    <p>Lorem Ipsum is simply dummy text of the printing and typesetting industry. Lorem Ipsum has been the industry's standard dummy text ever since the1500s.</p>
    <p>Lorem Ipsum is simply dummy text of the printing and typesetting industry.</p>
    <div class="letter__closing">Kind Regards</div>
    <div class="signatory__name">Darl Hensby</div>
    <div class="signatory__role">Manager</div>
    <span class="signature" role="img" aria-label="Handwritten signature of Darl Hensby"></span>
  </div>

  <ul class="contact">
    <li><svg viewBox="0 0 10 10"><path d="M2 0.5 L4 2.8 L3 4 C3.6 5.2 4.8 6.4 6 7 L7.2 6 L9.5 8 L8.5 9.5 C4.5 9.5 0.5 5.5 0.5 1.5Z"/></svg>0461 238 574</li>
    <li><svg viewBox="0 0 10 10"><path d="M0 4.5 L10 0 L6.5 10 L5 6 Z"/></svg>enquiries@scplumbwork.net.au</li>
    <li><svg viewBox="0 0 10 10"><path d="M4 6 L6 4 M3.5 4.5 L1.8 6.2 A1.6 1.6 0 0 0 3.8 8.2 L5.5 6.5 M6.5 5.5 L8.2 3.8 A1.6 1.6 0 0 0 6.2 1.8 L4.5 3.5" stroke="var(--brand-blue)" stroke-width="1.3" fill="none"/></svg>www.scplumbwork.net.au</li>
    <li><svg viewBox="0 0 10 10"><path d="M5 0.5 A3.5 3.5 0 0 1 8.5 4 C8.5 6.5 5 9.5 5 9.5 C5 9.5 1.5 6.5 1.5 4 A3.5 3.5 0 0 1 5 0.5Z M5 2.7 A1.3 1.3 0 1 0 5 5.3 A1.3 1.3 0 1 0 5 2.7Z" fill-rule="evenodd"/></svg>27 Quarry Lane,<br>Northam, WA 6401</li>
    <li class="contact__reg">ABN: 47 381 905 462</li>
    <li class="contact__reg">PCL: 5187</li>
  </ul>
</section>

<section class="card card--front" aria-label="Business card front">
  <div class="wordmark"><span class="wordmark__dot"></span>Silver Creek Plumbing</div>
</section>

<section class="card card--back" aria-label="Business card back">
  <div class="signatory__name">Darl Hensby</div>
  <div class="signatory__role">Manager</div>
  <ul class="contact">
    <li><svg viewBox="0 0 10 10"><path d="M2 0.5 L4 2.8 L3 4 C3.6 5.2 4.8 6.4 6 7 L7.2 6 L9.5 8 L8.5 9.5 C4.5 9.5 0.5 5.5 0.5 1.5Z"/></svg>0461 238 574</li>
    <li><svg viewBox="0 0 10 10"><path d="M0 4.5 L10 0 L6.5 10 L5 6 Z"/></svg>enquiries@scplumbwork.net.au</li>
    <li><svg viewBox="0 0 10 10"><path d="M4 6 L6 4 M3.5 4.5 L1.8 6.2 A1.6 1.6 0 0 0 3.8 8.2 L5.5 6.5 M6.5 5.5 L8.2 3.8 A1.6 1.6 0 0 0 6.2 1.8 L4.5 3.5" stroke="var(--brand-blue)" stroke-width="1.3" fill="none"/></svg>www.scplumbwork.net.au</li>
    <li><svg viewBox="0 0 10 10"><path d="M5 0.5 A3.5 3.5 0 0 1 8.5 4 C8.5 6.5 5 9.5 5 9.5 C5 9.5 1.5 6.5 1.5 4 A3.5 3.5 0 0 1 5 0.5Z M5 2.7 A1.3 1.3 0 1 0 5 5.3 A1.3 1.3 0 1 0 5 2.7Z" fill-rule="evenodd"/></svg>27 Quarry Lane, Northam, WA 6401</li>
    <li class="contact__reg">ABN: 47 381 905 462</li>
    <li class="contact__reg">PCL: 5187</li>
  </ul>
</section>

</body>
</html>
```